Gardener needs an exciting new flyer design.

I'm a passionate gardener that requires a custom flyer design for a owner operator gardening business. Design will be for a DL flyer. I'm based on the Sunshine coast in Queensland Australia. My target audience is the residential market on the Sunshine coast. Business name is Marlowe Greens. My services are, lawn mowing, weeding, Eco Friendly fertilizing, green waste removal, Mulching, tree and shrub pruning, Full garden makeovers, hedging, pressure cleaning, privacy screening, Timber deck rejuvenation, Planting, Turf preparation and installation, and much more. Free no obligation quotes, reliable and friendly service, great rates. 12 years experience. Web www.marlowegreens.com.au - Phone 0418527064 - Email doug@marlowegreens.com.au I would like the design to portray a friendly and professional approach.

Target Market(s)

Residential

Industry/Entity Type

Gardener

Font styles to use
Serif

Colors
9ccb3b
abd037
3176b5

Requirements
Must have
• my services, my logo, my contact details,

```html
<!DOCTYPE html>
<html lang="en">
<head>
<meta charset="utf-8">
<title>Marlowe Greens – DL Flyer</title>
<link href="https://fonts.googleapis.com/css2?family=Bebas+Neue&family=Roboto:wght@400;500;700&display=swap" rel="stylesheet">
<style>
  :root {
    --backdrop: #e5ded6;
    --purple-top: #4e2758;
    --purple-mid: #3e1c48;
    --purple-deep: #22082a;
    --green: #48a22f;
    --green-bright: #5cb83a;
    --sky-light: #dff0fa;
    --sky: #a9d6f0;
    --grass: #5fae2c;
    --grass-deep: #2e6a16;
    --white: #ffffff;
    --text-soft: #efe7f2;
  }
  * { box-sizing: border-box; margin: 0; padding: 0; }
  html, body { width: 1200px; height: 900px; overflow: hidden; }
  body {
    background: var(--backdrop);
    font-family: "Roboto", Arial, sans-serif;
    position: relative;
  }

  .flyer {
    position: absolute;
    top: 60px;
    width: 370px;
    height: 780px;
    overflow: hidden;
    box-shadow: 0 12px 30px rgba(60, 45, 40, 0.25);
  }
  .flyer--front { left: 190px; background: var(--purple-mid); }
  .flyer--back {
    left: 640px;
    background: linear-gradient(180deg, var(--purple-top) 0%, var(--purple-mid) 55%, var(--purple-deep) 100%);
    color: var(--white);
    text-align: center;
  }

  /* Front */
  .hero-photo {
    position: absolute;
    left: 0; top: 0;
    width: 100%; height: 480px;
    background: linear-gradient(180deg, var(--sky-light) 0%, var(--sky) 38%, #7fbf52 62%, var(--grass) 78%, var(--grass-deep) 100%);
  }
  .brand-name {
    position: absolute;
    top: 92px; left: 0; width: 100%;
    text-align: center;
    font-family: "Roboto", Arial, sans-serif;
    font-weight: 700;
    font-size: 24px;
    color: #3f8f2c;
  }
  .brand-name::before {
    content: "";
    display: inline-block;
    width: 14px; height: 14px;
    border-radius: 50%;
    background: #3f8f2c;
    margin-right: 8px;
    vertical-align: 1px;
  }
  .headline-disc {
    position: absolute;
    left: 30px; top: 150px;
    width: 310px; height: 310px;
    border-radius: 50%;
    background: rgba(64, 160, 40, 0.88);
    display: flex;
    align-items: center;
    justify-content: center;
    text-align: center;
  }
  .headline {
    font-family: "Bebas Neue", Impact, sans-serif;
    font-weight: 400;
    font-size: 44px;
    line-height: 0.95;
    color: var(--white);
    letter-spacing: 0.5px;
  }
  .front-body {
    position: absolute;
    left: 0; top: 420px;
    width: 100%; height: 360px;
  }
  .front-body svg { position: absolute; left: 0; top: 0; }
  .about {
    position: absolute;
    top: 100px; left: 34px; right: 34px;
    text-align: center;
    color: var(--text-soft);
    font-size: 13.5px;
    line-height: 1.45;
  }
  .about p + p { margin-top: 14px; }

  /* Back */
  .services-title {
    margin-top: 70px;
    font-family: "Bebas Neue", Impact, sans-serif;
    font-weight: 400;
    font-size: 50px;
    letter-spacing: 0.5px;
    line-height: 1;
  }
  .title-rule {
    width: 110px; height: 4px;
    background: var(--green);
    margin: 10px auto 18px;
  }
  .service-list {
    list-style: none;
    font-size: 16px;
    line-height: 1.55;
    color: var(--text-soft);
  }
  .service-list li::before { content: "* "; }
  .cta {
    margin: 38px auto 0;
    width: 290px;
    padding: 16px 0 14px;
    background: var(--green);
    font-family: "Bebas Neue", Impact, sans-serif;
    font-size: 40px;
    line-height: 0.95;
    letter-spacing: 0.5px;
  }
  .contact {
    margin-top: 18px;
    font-size: 15px;
    line-height: 1.6;
    color: var(--white);
  }
  .contact dt {
    display: inline;
    color: var(--green-bright);
    font-weight: 500;
  }
  .contact dd { display: inline; margin-left: 4px; }
  .contact div { display: block; }
  .footer-brand {
    position: absolute;
    bottom: 70px; left: 0; width: 100%;
    font-weight: 700;
    font-size: 26px;
    color: var(--white);
  }
  .footer-brand::before {
    content: "";
    display: inline-block;
    width: 16px; height: 16px;
    border-radius: 50%;
    background: var(--white);
    margin-right: 10px;
    vertical-align: 1px;
  }
</style>
</head>
<body>

<section class="flyer flyer--front">
  <div class="hero-photo" role="img" aria-label="Photo of lush green lawn under a bright blue sky with trees on the horizon"></div>
  <div class="brand-name">Marlowe Greens</div>
  <div class="headline-disc">
    <h1 class="headline">A beautiful<br>garden<br>doesn't happy<br>by itself</h1>
  </div>
  <div class="front-body">
    <svg width="370" height="360" viewBox="0 0 370 360" aria-hidden="true">
      <defs>
        <linearGradient id="frontPurple" x1="0" y1="0" x2="0" y2="1">
          <stop offset="0" stop-color="#55275f"/>
          <stop offset="0.6" stop-color="#3d1a47"/>
          <stop offset="1" stop-color="#26092e"/>
        </linearGradient>
      </defs>
      <path d="M0 30 Q185 110 370 10 L370 360 L0 360 Z" fill="url(#frontPurple)"/>
    </svg>
    <div class="about">
      <p>Marlowe Greens is your garden and lawn care specialist, with a passion for gardening and a keen eye for detail you can rest assured you're in the right hands.</p>
      <p>My services are tailored to meet every individual clients needs. From a one time mow too regular lawn mowing, all aspects of garden care and even full garden makeovers.</p>
      <p>I go that extra mile every time to leave your garden and yard looking amazing.</p>
    </div>
  </div>
</section>

<section class="flyer flyer--back">
  <h2 class="services-title">Our Services</h2>
  <div class="title-rule"></div>
  <ul class="service-list">
    <li>Lawn mowing</li>
    <li>Turf preparation and installation</li>
    <li>Tree and shrub pruning</li>
    <li>Fertilizing</li>
    <li>Full garden makeovers</li>
    <li>Green waste removal</li>
    <li>Garden mulching</li>
    <li>Hedging</li>
    <li>Weeding</li>
  </ul>
  <div class="cta">Schedule<br>an appoinment</div>
  <dl class="contact">
    <div><dt>Web:</dt><dd>www.marlowegreens.com.au</dd></div>
    <div><dt>Phone:</dt><dd>0418527064</dd></div>
    <div><dt>Email:</dt><dd>doug@marlowegreens.com.au</dd></div>
  </dl>
  <div class="footer-brand">Marlowe Greens</div>
</section>

</body>
</html>
```